Company Profile for Consulting Comany

Need Company profile to be designed in a professional way.

for inspiring :-
https://www.vimolia.net/gallery/5307462/COMPANY-PROFILE
https://www.vimolia.net/gallery/20934617/Biotech-Product-Catalog-No1-(Laminar-Air-Flow)
https://www.vimolia.net/gallery/38720954/RKT-Tramvale-Company-Profile-2014-(RKT-Rebrand-part-2)

Target Market(s)

Corporate

Industry/Entity Type

It Company

Font styles to use
Sans Serif

Requirements
Must have
• Landscape A4 size
• Must go with the logo branding
• Must Have Visual Identity is the most important
• Must Have mpty spaces

```html
<!DOCTYPE html>
<html lang="en">
<head>
<meta charset="utf-8">
<title>Shift Vector – Company Profile</title>
<link rel="stylesheet" href="https://fonts.googleapis.com/css2?family=Roboto:wght@300;400;500;700&display=swap">
<style>
:root{
  --cyan:#2bb5e0;
  --cyan-dark:#1d93ba;
  --ink:#151515;
  --coal:#222427;
  --text:#5a5a5a;
  --muted:#9a9a9a;
  --rule:#d6d6d6;
  --paper:#ffffff;
  --bg:#f3f3f3;
}
*{box-sizing:border-box;margin:0;padding:0}
html,body{width:1200px;height:2432px;overflow:hidden}
body{background:var(--bg);font-family:'Roboto',Arial,sans-serif;color:var(--text);position:relative}
.page{position:absolute;width:514px;height:370px;background:var(--paper);overflow:hidden;box-shadow:0 1px 3px rgba(0,0,0,.12)}
.page.left{left:62px}
.page.right{left:592px;width:546px}
.dark{background:var(--ink)}
.abs{position:absolute}
.para{font-size:5.6px;line-height:1.55;color:var(--text)}
.para b{color:var(--cyan);font-weight:500;display:block;font-size:6px;margin-top:6px}
.page-no{position:absolute;top:10px;right:16px;font-size:5px;color:var(--muted);letter-spacing:.5px}
.top-rule{position:absolute;top:20px;left:0;right:0;height:1px;background:var(--rule)}
.bar{position:absolute;top:20px;left:0;height:22px;background:var(--coal);color:var(--cyan);font-size:8px;letter-spacing:.6px;padding:7px 0 0 18px;text-transform:uppercase}
.h-thin{position:absolute;color:var(--cyan);font-weight:300;letter-spacing:.5px;text-transform:uppercase}
.brand{position:absolute;display:flex;align-items:center;gap:5px}
.brand .mark{background:var(--cyan)}
.brand .name{color:var(--cyan);font-weight:500;line-height:1}
.brand .tag{position:absolute;left:0;top:100%;color:var(--muted);white-space:nowrap}
.photo{position:absolute}
.cover-bg{position:absolute;inset:0;background:linear-gradient(160deg,#1b1e22 0%,#0c0d0f 55%,#23282e 100%)}
.frame{position:absolute;border:1px solid rgba(255,255,255,.22)}
.cover-band{position:absolute;left:0;top:154px;width:399px;height:88px;background:var(--cyan);color:#fff;padding:14px 0 0 30px}
.cover-band .small{font-size:11px;font-weight:300;letter-spacing:.5px}
.cover-band .big{font-size:26px;font-weight:300;margin-top:6px;letter-spacing:.3px}
.cover-foot{position:absolute;left:20px;bottom:18px;color:#cfcfcf;font-size:7.5px;letter-spacing:.8px}
.toc{position:absolute;left:56px;top:96px;width:420px;list-style:none}
.toc li{display:flex;font-size:6px;line-height:8.3px;color:#666}
.toc li span:first-child{flex:0 0 auto;padding-right:3px}
.toc li i{flex:1;border-bottom:1px dotted #c9c9c9;margin-bottom:2px}
.toc li span:last-child{padding-left:3px}
.mission{position:absolute;left:175px;top:97px;width:334px;height:195px;background:#0d0d0d;color:#e4e4e4;padding:10px 14px;font-size:5.4px;line-height:1.5}
.mission h4{font-size:6px;font-weight:500;color:#fff;margin-bottom:3px}
.mission .vals{margin-top:6px;border-top:1px solid #333}
.mission .vals div{display:flex;border-bottom:1px solid #333;padding:3px 0}
.mission .vals span:first-child{width:90px;color:#fff;font-weight:500}
.why-item{position:absolute;width:230px;display:flex;gap:8px}
.why-item .thumb{width:82px;height:70px;flex:0 0 auto}
.why-item h5{color:var(--cyan);font-size:6px;font-weight:500;margin:2px 0 3px;text-transform:uppercase}
.bullets{list-style:none;font-size:5.6px;line-height:1.7;color:var(--text)}
.bullets li::before{content:"• ";color:var(--cyan)}
.ta-panel{position:absolute;left:146px;top:170px;width:382px;height:120px;background:var(--cyan);display:grid;grid-template-columns:repeat(3,1fr);grid-template-rows:1fr 1fr;padding:8px}
.ta-cell{display:flex;flex-direction:column;align-items:center;justify-content:center;gap:4px;color:#fff;font-size:5px;text-transform:uppercase;letter-spacing:.3px}
.partner-name{position:absolute;left:70px;font-size:10px;font-weight:500;color:#2a4f8a;display:flex;align-items:center;gap:4px}
.partner-name i{width:9px;height:9px;background:#2a4f8a;display:inline-block}
.member{position:absolute;left:6px;width:530px;display:flex;gap:14px}
.member .face{width:54px;height:58px;flex:0 0 auto}
.member h5{color:var(--cyan);font-size:6.5px;font-weight:500;text-transform:uppercase;margin:4px 0 4px;letter-spacing:.3px}
.badge{position:absolute;height:16px;border-radius:2px}
.section-label{position:absolute;left:18px;font-size:7.5px;color:#333;letter-spacing:.4px}
.contact{position:absolute;left:14px;top:214px;width:160px;font-size:5.4px;line-height:1.55;color:var(--text)}
.contact h6{color:var(--cyan);font-size:8px;font-weight:400;margin-bottom:8px;letter-spacing:.5px}
.contact strong{color:#333;font-weight:500;display:block;margin-top:6px}
.back-panel{position:absolute;left:178px;top:0;width:368px;height:370px;background:linear-gradient(150deg,#3d4956 0%,#27303a 55%,#1b222a 100%)}
</style>
</head>
<body>

<section class="page left" style="top:44px;height:361px">
  <div class="cover-bg" role="img" aria-label="Dark city skyline backdrop"></div>
  <div class="frame" style="left:14px;top:14px;width:484px;height:318px"></div>
  <div class="frame" style="left:380px;top:255px;width:60px;height:50px"></div>
  <div class="frame" style="left:410px;top:275px;width:70px;height:60px"></div>
  <div class="brand" style="left:32px;top:46px">
    <span class="mark" style="width:30px;height:30px"></span>
    <span class="name" style="font-size:24px">Shift Vector</span>
    <span class="tag" style="font-size:7px;margin-top:3px;left:35px">Moving Ideas Forward</span>
  </div>
  <div class="cover-band">
    <div class="small">WE CAN HELP YOU TO</div>
    <div class="big">MAKE CHANGE HAPPEN</div>
  </div>
  <div class="cover-foot">STRATEGY | PEOPLE | TECHNOLOGY</div>
</section>

<section class="page left dark" style="top:435px">
  <div class="frame" style="left:100px;top:70px;width:310px;height:230px"></div>
  <div class="frame" style="left:160px;top:110px;width:250px;height:190px"></div>
  <div class="frame" style="left:260px;top:150px;width:230px;height:190px"></div>
  <div class="brand" style="left:420px;top:325px">
    <span class="mark" style="width:12px;height:12px"></span>
    <span class="name" style="font-size:9px">Shift Vector</span>
  </div>
</section>
<section class="page right" style="top:435px">
  <div class="bar" style="width:380px">Table of Contents</div>
  <div class="brand" style="left:420px;top:24px">
    <span class="mark" style="width:14px;height:14px"></span>
    <span class="name" style="font-size:10px">Shift Vector</span>
  </div>
  <ul class="toc">
    <li><span>Who we are?</span><i></i><span>2</span></li>
    <li><span>Executive Summary</span><i></i><span>2</span></li>
    <li><span>Vision</span><i></i><span>2</span></li>
    <li><span>Mission</span><i></i><span>2</span></li>
    <li><span>Values</span><i></i><span>2</span></li>
    <li><span>Why Shift Vector?</span><i></i><span>3</span></li>
    <li><span>What we do?</span><i></i><span>4</span></li>
    <li><span>HR &amp; OD Consultation</span><i></i><span>4</span></li>
    <li><span>Professional Training</span><i></i><span>4</span></li>
    <li><span>Talent Assessment</span><i></i><span>5</span></li>
    <li><span>HR Solutions</span><i></i><span>5</span></li>
    <li><span>Partnership</span><i></i><span>6</span></li>
    <li><span>Halvard Group</span><i></i><span>6</span></li>
    <li><span>Brantley Hale</span><i></i><span>6</span></li>
    <li><span>Quorra Talent</span><i></i><span>6</span></li>
    <li><span>Lumera Consulting</span><i></i><span>6</span></li>
    <li><span>Our Team</span><i></i><span>7</span></li>
    <li><span>Tarek Al Mansouri Consulting Manager</span><i></i><span>7</span></li>
    <li><span>Samir Haddad, Senior Consultant</span><i></i><span>7</span></li>
    <li><span>Faisal Al Rawi Projects Manager</span><i></i><span>7</span></li>
    <li><span>Idris Benkara Associate Consultant</span><i></i><span>7</span></li>
    <li><span>Certifications</span><i></i><span>8</span></li>
    <li><span>Our Clients</span><i></i><span>8</span></li>
    <li><span>Contact us</span><i></i><span>8</span></li>
  </ul>
</section>

<section class="page left" style="top:827px">
  <div class="page-no">PAGE 2</div>
  <div class="top-rule" style="top:22px;left:380px;right:16px;background:var(--cyan)"></div>
  <div class="h-thin" style="left:20px;top:46px;font-size:19px">Who we are?</div>
  <div class="para abs" style="left:20px;top:95px;width:140px">
    <span style="color:#333;font-weight:500">EXECUTIVE SUMMARY</span><br>
    Shift Vector is a professional HR and OD organisation based in the Gulf region, specialised in talent development, career coaching, leadership development and technology. We provide tailored services that help people and organisations change with confidence and clear purpose, working closely with local and global partners to deliver practical results that last.<br><br>
    <span style="color:#333;font-weight:500">VISION</span><br>
    "To become the leading HR consulting company in the region that turns bold ideas into quality change."
  </div>
  <div class="mission">
    <h4>MISSION</h4>
    We have a multi-layered mission statement reflecting the needs of our clients alongside a clear will to raise the value of our services and our standing among peers.<br>
    Our intentions are:<br>
    - To provide consistent HR solutions to SMEs so they can focus on the core of their business.<br>
    - To play our role in the economic development of the region and its neighbours.<br>
    - To develop a professional relationship with our valued clients and investors.<br>
    - To bring innovation to HR services through technology.
    <h4 style="margin-top:6px">VALUES</h4>
    <div class="vals">
      <div><span>INTEGRITY</span><span>We act with honesty with staff, clients, investors and partners.</span></div>
      <div><span>WORKPLACE ENVIRONMENT</span><span>We build a fair and respectful place where people can grow.</span></div>
      <div><span>ACCOUNTABILITY</span><span>Each of us owns the work we do and the results we deliver.</span></div>
      <div><span>PURSUIT OF EXCELLENCE</span><span>Our people strive for excellence in every task and every service.</span></div>
      <div><span>QUALITY CONTROL</span><span>We apply clear checks to keep each service at a high standard.</span></div>
      <div><span>AFFORDABILITY</span><span>Our services stay within reach of the budgets of local businesses.</span></div>
    </div>
  </div>
</section>
<section class="page right" style="top:827px">
  <div class="page-no">PAGE 3</div>
  <div class="bar" style="width:380px">Why Shift Vector?</div>
  <div class="brand" style="left:420px;top:24px">
    <span class="mark" style="width:14px;height:14px"></span>
    <span class="name" style="font-size:10px">Shift Vector</span>
  </div>
  <div class="why-item" style="left:57px;top:118px">
    <div class="thumb photo" style="position:static;background:linear-gradient(135deg,#5b7da3,#c8d3de)" role="img" aria-label="Business people shaking hands"></div>
    <div class="para"><h5>Success</h5>We will deliver results to you, as we achieved for clients before. Our success is tied to yours.</div>
  </div>
  <div class="why-item" style="left:290px;top:118px">
    <div class="thumb photo" style="position:static;background:linear-gradient(135deg,#9aa6b1,#3f4a55)" role="img" aria-label="Confident professional in office"></div>
    <div class="para"><h5>Superior Workforce</h5>Our skilled training professionals hold real experience and perform at their best every time.</div>
  </div>
  <div class="why-item" style="left:57px;top:210px">
    <div class="thumb photo" style="position:static;background:linear-gradient(135deg,#c4c9cf,#6e7b88)" role="img" aria-label="Team planning on paper"></div>
    <div class="para"><h5>Targeting</h5>We understand the importance of targeting the right people and processes for every client.</div>
  </div>
  <div class="why-item" style="left:290px;top:210px">
    <div class="thumb photo" style="position:static;background:linear-gradient(135deg,#4f89b5,#b6d3e6)" role="img" aria-label="Handshake over a desk"></div>
    <div class="para"><h5>Flexible Multi-Channel Abilities</h5>Our wide capabilities give us room to adapt to each client and goal.</div>
  </div>
  <div class="why-item" style="left:290px;top:292px">
    <div class="thumb" style="width:82px;height:0"></div>
    <div class="para"><h5>Cost Effectiveness</h5>Lean teams and fair rates keep every project within a sensible budget.</div>
  </div>
</section>

<section class="page left" style="top:1220px">
  <div class="brand" style="left:16px;top:12px">
    <span class="mark" style="width:18px;height:18px"></span>
    <span class="name" style="font-size:12px">Shift Vector</span>
  </div>
  <div class="top-rule" style="top:40px;left:16px;right:16px;background:var(--cyan)"></div>
  <div class="page-no">PAGE 4</div>
  <div class="photo" style="left:230px;top:21px;width:284px;height:187px;background:linear-gradient(135deg,#eef0f2,#b9c0c7)" role="img" aria-label="Hands reviewing documents and charts"></div>
  <div class="h-thin" style="left:16px;top:54px;font-size:19px">What we do?</div>
  <div class="para abs" style="left:16px;top:84px;width:200px"><span style="color:#333;font-weight:500">HR &amp; OD CONSULTATION</span><br>Our dedicated team of HR and OD experts is on hand to provide professional support for your HR and OD functions and development.</div>
  <ul class="bullets abs" style="left:16px;top:128px;width:200px">
    <li>HR Strategic Alignment</li>
    <li>Organizational Design &amp; Restructuring</li>
    <li>Talent Assessment &amp; Management</li>
    <li>Learning &amp; Leadership Development</li>
    <li>Communication &amp; Change Management</li>
    <li>Compensation &amp; Benefits</li>
    <li>Work life initiatives</li>
    <li>Performance &amp; Recognition</li>
    <li>Development &amp; Career Opportunities</li>
    <li>Coaching &amp; Mentoring Program</li>
  </ul>
  <div class="para abs" style="left:198px;top:222px;width:300px">
    <b>PROFESSIONAL TRAINING</b>Our vocational training services will enable people and organisations to maximise the skills, knowledge and abilities of their workforce through practical sessions.
    <b>IN HOUSE CUSTOM TRAINING</b>We are committed to provide a high quality training that adds value to our client's employees and their business processes. Our tailored programs make a difference.
    <b>PROFESSIONAL QUALIFICATIONS</b>We are proud to introduce a global portfolio of certified qualifications that are widely recognised for their significant benefit to learners.
  </div>
</section>
<section class="page right" style="top:1220px">
  <div class="page-no">PAGE 5</div>
  <div class="abs" style="left:16px;top:16px;font-size:8px;color:#333;letter-spacing:.5px">TALENT ASSESSMENT</div>
  <div class="top-rule" style="top:30px;left:16px;right:16px"></div>
  <div class="para abs" style="left:16px;top:44px;width:115px">Our carefully developed assessment solutions allow you to assess the skills, aptitudes and abilities of your workforce, enabling you to identify and fill any skills gaps.</div>
  <div class="para abs" style="left:146px;top:40px;width:382px">
    <b>TALENT ASSESSMENT</b>Assessing people for their performance is the most important task of any organisation. Selecting the right talent determines results across every function and team level.
    <b>TALENT MANAGEMENT</b>As an organisation grows, the need to develop people becomes clear. A structured process helps retain, engage and reward people who drive success.
    <b>HR SOLUTIONS</b>Our full suite HRMS solution, combined with regional expertise, brings payroll, attendance and self service together in one simple and secure platform for local businesses.
  </div>
  <div class="ta-panel">
    <div class="ta-cell"><svg width="16" height="16" viewBox="0 0 16 16"><circle cx="8" cy="5" r="3" fill="#fff"/><rect x="3" y="10" width="10" height="5" rx="2" fill="#fff"/></svg>Employee Relations</div>
    <div class="ta-cell"><svg width="16" height="16" viewBox="0 0 16 16"><rect x="2" y="3" width="12" height="10" rx="1" fill="none" stroke="#fff" stroke-width="1.5"/><line x1="2" y1="7" x2="14" y2="7" stroke="#fff" stroke-width="1.5"/></svg>Payroll History</div>
    <div class="ta-cell"><svg width="16" height="16" viewBox="0 0 16 16"><rect x="2" y="9" width="3" height="5" fill="#fff"/><rect x="6.5" y="6" width="3" height="8" fill="#fff"/><rect x="11" y="3" width="3" height="11" fill="#fff"/></svg>Reports</div>
    <div class="ta-cell"><svg width="16" height="16" viewBox="0 0 16 16"><polyline points="3,8 7,12 13,4" fill="none" stroke="#fff" stroke-width="2"/></svg>Onboarding &amp; Exits</div>
    <div class="ta-cell"><svg width="16" height="16" viewBox="0 0 16 16"><circle cx="7" cy="7" r="4.5" fill="none" stroke="#fff" stroke-width="1.5"/><line x1="10.5" y1="10.5" x2="14" y2="14" stroke="#fff" stroke-width="1.8"/></svg>Recruitment &amp; Hiring</div>
    <div class="ta-cell"><svg width="16" height="16" viewBox="0 0 16 16"><path d="M8 8 L8 2 A6 6 0 1 1 2 8 Z" fill="#fff"/></svg>Performance Management</div>
  </div>
</section>

<section class="page left" style="top:1606px">
  <div class="page-no">PAGE 6</div>
  <div class="bar" style="width:360px">Success Partnership</div>
  <div class="brand" style="left:400px;top:24px">
    <span class="mark" style="width:14px;height:14px"></span>
    <span class="name" style="font-size:10px">Shift Vector</span>
  </div>
  <div class="partner-name" style="top:84px"><i></i>Halvard</div>
  <div class="partner-name" style="top:118px"><i></i>Kestra</div>
  <div class="partner-name" style="top:154px"><i></i>Brantley Hale</div>
  <div class="partner-name" style="top:194px"><i></i>Tidemark</div>
  <div class="partner-name" style="top:232px"><i></i>Quorra</div>
  <div class="partner-name" style="top:266px"><i></i>Lumera</div>
  <div class="para abs" style="left:214px;top:62px;width:290px">
    <b>HALVARD GROUP</b>Halvard is an international consulting firm that guides organisations through all types of change and has helped clients around the world apply its proven methods.
    <b>BRANTLEY HALE</b>Brantley Hale has been helping clients turn their strategy into action for decades, focusing on leadership and the culture that drives long term performance.
    <b>KESTRA</b>With over ten years of experience helping clients, Kestra offers assessment and development tools that raise the quality of hiring and coaching decisions.
    <b>QUORRA TALENT</b>Quorra is a comprehensive human capital platform that simplifies core HR processes and gives leaders clear insight into their workforce.
    <b>LUMERA CONSULTING</b>Lumera is an organisation specialised in providing innovative leadership development solutions to companies across the region.
  </div>
</section>
<section class="page right" style="top:1606px">
  <div class="page-no" style="color:#ccc">PAGE 7</div>
  <div class="photo" style="left:0;top:0;width:546px;height:105px;background:linear-gradient(180deg,#2d3339 0%,#4a525a 100%)" role="img" aria-label="Team meeting around a table"></div>
  <div class="h-thin" style="left:14px;top:58px;font-size:30px">Our Team</div>
  <div class="member" style="top:122px">
    <div class="face photo" style="position:static;background:linear-gradient(180deg,#d9d9d9,#9a9a9a)" role="img" aria-label="Portrait of consulting manager"></div>
    <div class="para"><h5>Tarek Al Mansouri – Consulting Manager</h5>Certified HR practitioner with over fifteen years of exceptional local and international business experience in talent, organisation design and change across finance, energy, retail and technology sectors, leading transformation programmes from strategy to delivery.</div>
  </div>
  <div class="member" style="top:198px">
    <div class="face photo" style="position:static;background:linear-gradient(180deg,#d4d4d4,#8f8f8f)" role="img" aria-label="Portrait of senior consultant"></div>
    <div class="para"><h5>Samir Haddad – Senior Consultant</h5>Certified HR practitioner with over twelve years of experience in assessment and development, holding qualifications in coaching, change management and leadership to support positive change in people and teams.</div>
  </div>
  <div class="member" style="top:274px">
    <div class="face photo" style="position:static;background:linear-gradient(180deg,#e2e2e2,#a3a3a3)" role="img" aria-label="Portrait of projects manager"></div>
    <div class="para"><h5>Faisal Al Rawi – Projects Manager</h5>Certified project manager and IT professional with over ten years of experience delivering enterprise systems, training rollouts and HR technology projects for medium and large organisations across the region.</div>
  </div>
</section>

<section class="page left" style="top:1998px">
  <div class="page-no">PAGE 8</div>
  <div class="section-label" style="top:22px">CERTIFICATIONS</div>
  <div class="top-rule" style="top:34px;left:18px;right:16px"></div>
  <div class="badge" style="left:18px;top:56px;width:50px;background:#1e3f7a"></div>
  <div class="badge" style="left:78px;top:56px;width:50px;background:#2d6fa5"></div>
  <div class="badge" style="left:138px;top:56px;width:44px;background:#b3262b"></div>
  <div class="badge" style="left:192px;top:56px;width:48px;background:#333"></div>
  <div class="badge" style="left:250px;top:56px;width:20px;background:#7b2a85"></div>
  <div class="badge" style="left:278px;top:56px;width:44px;background:#8a3d8f"></div>
  <div class="badge" style="left:332px;top:56px;width:20px;background:#4a2b78;border-radius:50%"></div>
  <div class="badge" style="left:18px;top:82px;width:50px;background:#2f5fa0"></div>
  <div class="badge" style="left:78px;top:82px;width:40px;background:#1c6db5"></div>
  <div class="badge" style="left:128px;top:82px;width:38px;background:#333"></div>
  <div class="badge" style="left:176px;top:82px;width:30px;height:22px;background:#c32127"></div>
  <div class="badge" style="left:216px;top:82px;width:46px;background:#2a4f8a"></div>
  <div class="badge" style="left:18px;top:106px;width:58px;background:#1f3e6e"></div>
  <div class="section-label" style="top:216px">OUR CLIENTS</div>
  <div class="top-rule" style="top:228px;left:18px;right:16px"></div>
  <div class="badge" style="left:18px;top:254px;width:34px;height:24px;background:#3f8a4a;border-radius:50%"></div>
  <div class="badge" style="left:66px;top:254px;width:46px;height:24px;background:#1f4f8f"></div>
  <div class="badge" style="left:126px;top:254px;width:34px;height:24px;background:#c99a2e"></div>
  <div class="badge" style="left:176px;top:254px;width:34px;height:24px;background:#2b8a8a"></div>
  <div class="badge" style="left:226px;top:254px;width:34px;height:24px;background:#e0771f"></div>
  <div class="badge" style="left:272px;top:254px;width:40px;height:24px;background:#1e6aa8"></div>
  <div class="badge" style="left:18px;top:290px;width:40px;height:24px;background:#1d3c6b"></div>
</section>
<section class="page right" style="top:1998px">
  <div class="abs" style="left:0;top:0;width:178px;height:370px;background:#f6f6f6"></div>
  <div class="contact">
    <h6>CONTACT US</h6>
    <strong>DUBAI</strong>
    PO Box 40718, Dubai<br>
    23rd Floor, Harbour Tower 2, Marina Road<br>
    T: 0000 4 100 2000<br>
    F: 0000 4 100 2001<br>
    E: hello@shiftvector.example
    <strong style="margin-top:14px">KHOBAR</strong>
    PO Box 77215, Khobar<br>
    21st Floor, Corniche Tower, Gulf Street<br>
    T: 0000 13 200 3000<br>
    E: hello@shiftvector.example<br>
    www.shiftvector.example
  </div>
  <div class="back-panel" role="img" aria-label="Dark textured backdrop"></div>
  <div class="brand" style="left:280px;top:160px;flex-direction:column;gap:6px">
    <span class="mark" style="width:40px;height:40px"></span>
    <span class="name" style="font-size:20px">Shift Vector</span>
    <span style="font-size:7px;color:#c8d6e0;letter-spacing:.5px">Moving Ideas Forward</span>
  </div>
</section>

</body>
</html>
```